Business Cards for Communications Technology Company

We are an innovative software company based in Tropical North Queensland, Australia. We have several brands with a focus on communications software for businesses. We are looking for a business card that is very innovate and creative whilst still remaining professional on a corporate level.

Our internal culture is very progressive and expresses a blend between the clarity of our natural surroundings and the highly technological industry we work in. Our current branding blends a modern minimalist typeface with the desire to push the boundaries in the way we communicate.

This is a corporate level business card for the communications software industry and may possibly also encompass our brands MarNetwork, PelFax, TukMailer and our B2B marketing service—with our companies name being Viresca Partners. Showing other brands on the business card is optional not compulsory.

Technical notes:

-We will attach all logo's and some examples of our corporate branding
- Would be willing to print with various papers, embossed, metallic ink, curved edges etc. in a standard business card size

Sample content:

Rowan Pellick
Senior Account Manager
Phone: 1300 842 916 / +617 4583 2764
Email: r.pellick@viresca.com.au
Web: www.viresca.com.au

Sincerely,
Viresca Partners.

```html
<!DOCTYPE html>
<html lang="en">
<head>
<meta charset="utf-8">
<title>Viresca Partners – Business Card</title>
<link rel="stylesheet" href="https://fonts.googleapis.com/css2?family=Lato:wght@400;700;900&display=swap">
<style>
  :root {
    --bg: #1c1e20;
    --card: #24282b;
    --card-edge: #2e3336;
    --ink: #ffffff;
    --ink-soft: #b9bdc0;
    --ink-dim: #6b7074;
    --green: #7ac143;
    --blue: #3f73c4;
    --orange: #f26c21;
  }
  * { box-sizing: border-box; margin: 0; padding: 0; }
  html, body {
    width: 1200px; height: 1076px; overflow: hidden;
    background: var(--bg);
    font-family: "Lato", sans-serif;
  }
  .sheet {
    width: 1200px; height: 1076px;
    display: flex; flex-direction: column; align-items: center; justify-content: center;
    gap: 44px;
  }
  .card {
    position: relative;
    width: 860px; height: 470px;
    background: var(--card);
    border: 1px solid var(--card-edge);
    border-radius: 4px;
    overflow: hidden;
  }

  /* Front */
  .card--front { display: flex; align-items: center; justify-content: center; }
  .wordmark { display: flex; align-items: center; gap: 18px; }
  .wordmark__dot { width: 62px; height: 62px; border-radius: 50%; }
  .wordmark__name { font-weight: 400; letter-spacing: 1px; }
  .card--front .wordmark__dot { background: #3a3f43; }
  .card--front .wordmark__name { font-size: 64px; color: var(--ink-soft); }

  /* Back */
  .card--back .wordmark { position: absolute; left: 62px; top: 56px; }
  .card--back .wordmark__dot { background: var(--green); width: 56px; height: 56px; }
  .card--back .wordmark__name { font-size: 54px; color: var(--ink); }

  .faint-circle {
    position: absolute; right: -40px; top: 110px;
    width: 420px; height: 420px; border-radius: 50%;
    background: #2a2f32;
  }

  .person { position: absolute; left: 62px; top: 170px; }
  .person__name { font-weight: 700; font-size: 31px; color: var(--ink); letter-spacing: 0.5px; }
  .person__role { font-size: 25px; color: var(--green); margin-top: 2px; letter-spacing: 0.5px; }

  .contact { position: absolute; left: 46px; top: 262px; list-style: none; }
  .contact__row { display: flex; align-items: center; gap: 12px; font-size: 24px; color: var(--ink); line-height: 32px; }
  .contact__icon { width: 24px; height: 24px; flex: none; }
  .contact__web { margin-top: 4px; margin-left: -12px; }
  .contact__web em { font-style: normal; color: var(--green); }

  .brands {
    position: absolute; left: 50px; right: 50px; bottom: 36px;
    display: flex; justify-content: space-between; align-items: center;
  }
  .brand { display: flex; align-items: center; gap: 10px; font-weight: 700; font-size: 40px; }
  .brand__dot { width: 18px; height: 18px; border-radius: 50%; }
  .brand--mail { color: var(--blue); } .brand--mail .brand__dot { background: var(--blue); }
  .brand--fax { color: var(--green); } .brand--fax .brand__dot { background: var(--green); }
  .brand--net { color: var(--orange); } .brand--net .brand__dot { background: var(--orange); }
</style>
</head>
<body>
<main class="sheet">
  <section class="card card--front" aria-label="Card front">
    <div class="wordmark">
      <span class="wordmark__dot"></span>
      <span class="wordmark__name">Viresca Partners</span>
    </div>
  </section>

  <section class="card card--back" aria-label="Card back">
    <div class="faint-circle"></div>
    <div class="wordmark">
      <span class="wordmark__dot"></span>
      <span class="wordmark__name">Viresca Partners</span>
    </div>

    <div class="person">
      <p class="person__name">Rowan Pellick</p>
      <p class="person__role">Senior Account Manager</p>
    </div>

    <ul class="contact">
      <li class="contact__row">
        <svg class="contact__icon" viewBox="0 0 24 24" aria-hidden="true">
          <circle cx="12" cy="12" r="10.5" fill="none" stroke="#7ac143" stroke-width="1.8"/>
          <path d="M7 9.5c0-1.2 2.2-2.2 5-2.2s5 1 5 2.2l-1.6.8-1.2-1.2H9.8L8.6 10.3z M8.5 11h7l1 4.5h-9z" fill="#7ac143"/>
        </svg>
        <span>1300 842 916 / +617 4583 2764</span>
      </li>
      <li class="contact__row">
        <svg class="contact__icon" viewBox="0 0 24 24" aria-hidden="true">
          <circle cx="12" cy="12" r="10.5" fill="none" stroke="#7ac143" stroke-width="1.8"/>
          <rect x="6.5" y="8" width="11" height="8" fill="#7ac143"/>
          <path d="M6.5 8l5.5 4.5L17.5 8" fill="none" stroke="#24282b" stroke-width="1.2"/>
        </svg>
        <span>r.pellick@viresca.com.au</span>
      </li>
      <li class="contact__row contact__web">
        <span>www.<em>viresca</em>.com.au</span>
      </li>
    </ul>

    <div class="brands">
      <span class="brand brand--mail">TukMailer<span class="brand__dot"></span></span>
      <span class="brand brand--fax">PelFax<span class="brand__dot"></span></span>
      <span class="brand brand--net">MarNetwork<span class="brand__dot"></span></span>
    </div>
  </section>
</main>
</body>
</html>
```